Social Media Graphics - ALL TEXT RK

We are looking for a series of social media graphics for Instagram (standard size 1:1 (1080x1080px) that are ALL TEXT. We want the following quotes below on each graphic; one quote per graphic. AND, In very small letters at the bottom of each graphic, add @RKMarlowLive

The look and feel of these graphics should be complimentary to the color palette attached below; but keep them simple. But the design is up to you; at the end of this document, I provided various samples of all text graphics that I like as examples.

Target Market(s)

women looking to lose weight

Industry/Entity Type

health and wellness

Colors
E54698
E96AAD
F1A4CE
F9D9EA
FCEFF6

Requirements
Must have
• the quotes in the document
Should not have
• no stock photography

```html
<!DOCTYPE html>
<html lang="en">
<head>
<meta charset="utf-8">
<title>RK All-Text Social Graphics</title>
<link rel="stylesheet" href="https://fonts.googleapis.com/css2?family=Anton&family=Inter:wght@500&display=swap">
<style>
  :root {
    --pink-deep: #E54698;
    --pink-mid: #E96AAD;
    --pink-soft: #FCEFF6;
    --page: #FFFFFF;
    --white: #FFFFFF;
  }
  * { margin: 0; padding: 0; box-sizing: border-box; }
  html, body {
    width: 1200px;
    height: 917px;
    overflow: hidden;
    background: var(--page);
  }
  .sheet {
    position: relative;
    width: 1200px;
    height: 917px;
    display: grid;
    grid-template-columns: repeat(4, 273px);
    grid-auto-rows: 273px;
    gap: 5px 5px;
    padding: 33px 0 0 47px;
  }
  .post {
    position: relative;
    width: 273px;
    height: 273px;
    background: var(--pink-soft);
  }
  .post__quote {
    position: absolute;
    left: 0;
    top: 0;
    width: 100%;
    height: 227px;
    display: flex;
    align-items: center;
    justify-content: center;
    padding: 0 8px;
    text-align: center;
    font-family: "Anton", "Oswald", sans-serif;
    font-size: 22px;
    line-height: 30px;
    letter-spacing: 0.1px;
    color: var(--pink-deep);
  }
  .post__band {
    position: absolute;
    left: 0;
    top: 227px;
    width: 100%;
    height: 19px;
    background: var(--pink-mid);
    display: flex;
    align-items: center;
    justify-content: center;
    font-family: "Inter", "Helvetica Neue", Arial, sans-serif;
    font-weight: 500;
    font-size: 7px;
    color: var(--white);
  }
</style>
</head>
<body>
<main class="sheet">
  <article class="post">
    <p class="post__quote">Wake up tomorrow<br>with a flatter belly- yes,<br>this overnight remedy<br>works like magic!</p>
    <div class="post__band">@RKMarlowLive</div>
  </article>
  <article class="post">
    <p class="post__quote">Struggling with bloating<br>and belly fat?<br>Try this natural solution<br>tonight, and wake up<br>feeling lighter!</p>
    <div class="post__band">@RKMarlowLive</div>
  </article>
  <article class="post">
    <p class="post__quote">One supplement,<br>one night; your belly<br>bloat could be gone by<br>morning. Here's how it<br>works!</p>
    <div class="post__band">@RKMarlowLive</div>
  </article>
  <article class="post">
    <p class="post__quote">Finally-a natural<br>solution that flattens<br>your belly AND eases<br>stomach bloat</p>
    <div class="post__band">@RKMarlowLive</div>
  </article>
  <article class="post">
    <p class="post__quote">Sis, your hormones are<br>out of whack - that's<br>why the weight won't<br>budge!</p>
    <div class="post__band">@RKMarlowLive</div>
  </article>
  <article class="post">
    <p class="post__quote">Frustrated with belly fat<br>that won't budge? I've<br>got the solution that<br>finally worked for<br>me-no crazy diets<br>required.</p>
    <div class="post__band">@RKMarlowLive</div>
  </article>
  <article class="post">
    <p class="post__quote">That stubborn belly fat<br>isn't your fault - here's<br>what no one tells you.</p>
    <div class="post__band">@RKMarlowLive</div>
  </article>
  <article class="post">
    <p class="post__quote">You've been lied<br>to - 'just eat less and<br>exercise more' doesn't<br>work in menopause</p>
    <div class="post__band">@RKMarlowLive</div>
  </article>
  <article class="post">
    <p class="post__quote">A natural way to boost<br>GLP-1 - no injections, no<br>side effects, just real<br>results. Here's how it<br>works</p>
    <div class="post__band">@RKMarlowLive</div>
  </article>
  <article class="post">
    <p class="post__quote">GLP-1: the magic behind<br>the weight loss drugs.<br>But here's the secret -<br>you can boost it<br>naturally without a<br>prescription!</p>
    <div class="post__band">@RKMarlowLive</div>
  </article>
</main>
</body>
</html>
```